Business Card Design needed - Something Awesome!

Need a business card designed. Company is "Harbor Vane Consulting" we do consulting and also have sales automation technology.
I'm going to use thick stock or metal, something really nice... I was thinking about a QR Code on the back that would just upload my contact info to the persons contact, etc -

This is a Strategy Company with a tech feel. I'm open to ideas but really want this to be nice!

I need a template that should include:

Name | Position or Title
D: 555.203.8146
www.harborvaneconsulting.example

I'm going to attach my contact so you can use that one, I need to get this printed.

Target Market(s)

Small to mid size customers, Entrepreneurs etc.

Industry/Entity Type

Consulting, Tech, Private Equity.

Contact Information for Business Card

Name, Phone, Maybe email, URL

Font styles to use
Sans Serif

Colors

Designer to choose only greyscale colors for use in the design.

Requirements
Must have
• Fresh, Clean, stand out from the crowd - will be on thick stock or metal.
Nice to have
• Clean, simple yet impactful.
Should not have
• Not cartoonish

```html
<!DOCTYPE html>
<html lang="en">
<head>
<meta charset="utf-8">
<title>Harbor Vane Consulting – Business Card</title>
<link href="https://fonts.googleapis.com/css2?family=Montserrat:wght@400;500;700&display=swap" rel="stylesheet">
<style>
  :root {
    --backdrop: #3a3a3a;
    --card: #121212;
    --silver: #c9c9c9;
    --silver-dim: #9a9a9a;
    --rule: #6a6a6a;
    --gloss: #2a2a2a;
  }
  * { margin: 0; padding: 0; box-sizing: border-box; }
  html, body {
    width: 1200px; height: 801px; overflow: hidden;
    background: var(--backdrop);
    font-family: "Montserrat", sans-serif;
  }
  .stage {
    position: relative; width: 1200px; height: 801px;
    display: flex; align-items: center; justify-content: center; gap: 60px;
  }
  .card {
    position: relative; width: 500px; height: 286px;
    background: var(--card);
    box-shadow: 0 10px 30px rgba(0,0,0,.45);
  }
  /* Front */
  .brand-name {
    position: absolute; left: 44px; top: 70px;
    font-size: 38px; font-weight: 500; letter-spacing: 3px;
    color: var(--silver);
  }
  .details {
    position: absolute; left: 44px; right: 30px; top: 168px;
    display: flex; align-items: center;
  }
  .person { text-align: right; padding-right: 18px; width: 205px; }
  .person-name {
    font-size: 15px; font-weight: 700; letter-spacing: .5px;
    color: var(--silver); text-transform: uppercase;
  }
  .person-title { font-size: 12px; color: var(--silver-dim); margin-top: 3px; }
  .divider { width: 1px; height: 54px; background: var(--rule); }
  .contact { list-style: none; padding-left: 16px; }
  .contact li {
    display: flex; align-items: center; gap: 7px;
    font-size: 10.5px; color: var(--silver); line-height: 18px; white-space: nowrap;
  }
  .contact svg { width: 10px; height: 10px; flex: none; }
  /* Back */
  .back-mark {
    position: absolute; inset: 0;
    display: flex; align-items: center; justify-content: center; gap: 12px;
  }
  .back-square { width: 18px; height: 18px; background: var(--gloss); }
  .back-name {
    font-size: 22px; font-weight: 500; letter-spacing: 3px; color: var(--gloss);
  }
</style>
</head>
<body>
<main class="stage">
  <section class="card card-front" aria-label="Card front">
    <div class="brand-name">HARBOR VANE</div>
    <div class="details">
      <div class="person">
        <div class="person-name">Darren K. Holloway</div>
        <div class="person-title">Founder / CEO</div>
      </div>
      <div class="divider"></div>
      <ul class="contact">
        <li>
          <svg viewBox="0 0 10 10"><circle cx="5" cy="5" r="5" fill="#c9c9c9"/><path d="M3 2.5l1 1-.6.8c.4.8 1 1.4 1.8 1.8l.8-.6 1 1-.7.9C4.6 7.3 2.7 5.4 2.6 3.2z" fill="#121212"/></svg>
          555.203.8146
        </li>
        <li>
          <svg viewBox="0 0 10 10"><rect x="0.5" y="2" width="9" height="6" fill="#c9c9c9"/><path d="M0.5 2l4.5 3.3L9.5 2" stroke="#121212" stroke-width="0.9" fill="none"/></svg>
          info@harborvaneconsulting.example
        </li>
        <li>
          <svg viewBox="0 0 10 10"><circle cx="5" cy="5" r="5" fill="#c9c9c9"/><path d="M0.5 5h9M5 0.5c-2.4 2.6-2.4 6.4 0 9M5 0.5c2.4 2.6 2.4 6.4 0 9" stroke="#121212" stroke-width="0.7" fill="none"/></svg>
          www.harborvaneconsulting.example
        </li>
      </ul>
    </div>
  </section>
  <section class="card card-back" aria-label="Card back">
    <div class="back-mark">
      <span class="back-square"></span>
      <span class="back-name">HARBOR VANE</span>
    </div>
  </section>
</main>
</body>
</html>
```